Creating a Label for the Wine "Viña Aldaluz"

Viña Aldaluz
Viña Aldaluz means “lost mountain. Viña Aldaluz is a mountain far away from everything, lost in a wild place. The dimensios shoul be between 9cm x 11,5 cm and 12cm x 8 cm.

```html
<!DOCTYPE html>
<html lang="es">
<head>
<meta charset="utf-8">
<title>Viña Aldaluz – Cabernet Sauvignon label</title>
<link href="https://fonts.googleapis.com/css2?family=Dancing+Script:wght@500&family=Dosis:wght@400;500&display=swap" rel="stylesheet">
<style>
  :root {
    --backdrop: #f4f1ea;
    --paper: #e8dcc6;
    --ink: #2a2a2a;
    --rule: #3a3a3a;
    --placeholder: #cdbfa5;
  }
  html, body {
    margin: 0;
    width: 1200px;
    height: 943px;
    overflow: hidden;
    background: var(--backdrop);
  }
  .label {
    position: absolute;
    left: 360px;
    top: 101px;
    width: 480px;
    height: 740px;
    background: var(--paper);
    color: var(--ink);
    font-family: "Dosis", sans-serif;
    box-shadow: 0 2px 10px rgba(0,0,0,0.08);
  }
  .label__emblem {
    position: absolute;
    left: 155px;
    top: 75px;
    width: 176px;
    height: 119px;
    background: var(--placeholder);
  }
  .rule {
    position: absolute;
    height: 2px;
    background: var(--rule);
  }
  .rule--top { left: 13px; top: 194px; width: 459px; }
  .rule--left { left: 13px; top: 381px; width: 168px; }
  .rule--right { left: 306px; top: 381px; width: 166px; }
  .label__ornament {
    position: absolute;
    left: 215px;
    top: 360px;
    width: 46px;
    height: 46px;
    background: var(--placeholder);
  }
  .label__name {
    position: absolute;
    left: 0;
    top: 240px;
    width: 480px;
    margin: 0;
    text-align: center;
    font-family: "Dancing Script", cursive;
    font-weight: 500;
    font-size: 80px;
    line-height: 100px;
  }
  .label__vintage,
  .label__variety {
    position: absolute;
    left: 0;
    width: 480px;
    text-align: center;
    margin: 0;
    font-weight: 500;
  }
  .label__vintage { top: 446px; font-size: 34px; line-height: 44px; }
  .label__variety { top: 537px; font-size: 31px; line-height: 40px; }
  .label__volume,
  .label__abv {
    position: absolute;
    top: 674px;
    font-size: 20px;
    line-height: 26px;
    font-weight: 400;
    margin: 0;
  }
  .label__volume { left: 13px; }
  .label__abv { right: 13px; }
</style>
</head>
<body>
  <section class="label">
    <div class="label__emblem" role="img" aria-label="Winery emblem area"></div>
    <div class="rule rule--top"></div>
    <h1 class="label__name">Viña Aldaluz</h1>
    <div class="rule rule--left"></div>
    <div class="label__ornament" role="img" aria-label="Vine leaf ornament"></div>
    <div class="rule rule--right"></div>
    <p class="label__vintage">2009</p>
    <p class="label__variety">Cabernet Sauvignon</p>
    <p class="label__volume">0,75lt.</p>
    <p class="label__abv">13% Vol.</p>
  </section>
</body>
</html>
```